Mosvane Design

Looking for Mosvane banner and square design:
Mosvane Banner
W:1600 px H:400 px
Square
120x120

Logo attached.

Description: Data-Driven stock market portfolio management using quantitative analysis.

```html
<!DOCTYPE html>
<html lang="en">
<head>
<meta charset="utf-8">
<title>Mosvane Banner</title>
<link href="https://fonts.googleapis.com/css2?family=Poppins:wght@400;500;700&display=swap" rel="stylesheet">
<style>
  :root {
    --stage: #121212;
    --navy: #0a4f97;
    --blue: #0b5fae;
    --blue-mid: #1273c4;
    --sky: #80c6fb;
    --white: #ffffff;
  }
  * { margin: 0; padding: 0; box-sizing: border-box; }
  html, body {
    width: 1200px;
    height: 1200px;
    overflow: hidden;
    background: var(--stage);
  }
  .banner {
    position: absolute;
    left: 25px;
    top: 456px;
    width: 1151px;
    height: 287px;
    overflow: hidden;
    font-family: "Poppins", sans-serif;
    color: var(--white);
  }
  .banner-backdrop {
    position: absolute;
    inset: 0;
    background:
      radial-gradient(ellipse 60% 70% at 45% 40%, rgba(40,140,210,0.45), transparent 70%),
      linear-gradient(90deg, var(--blue) 0%, var(--navy) 50%, var(--blue) 100%);
  }
  .banner-wave {
    position: absolute;
    inset: 0;
    width: 1151px;
    height: 287px;
  }
  .headline {
    position: absolute;
    left: 71px;
    top: 75px;
    font-size: 26px;
    line-height: 33px;
    white-space: nowrap;
  }
  .headline-strong { font-weight: 700; letter-spacing: 0.2px; display: block; }
  .headline-light { font-weight: 400; display: block; }
  .divider {
    position: absolute;
    left: 694px;
    top: 52px;
    width: 2px;
    height: 117px;
    background: var(--white);
  }
  .brand-dot {
    position: absolute;
    left: 716px;
    top: 75px;
    width: 70px;
    height: 70px;
    border-radius: 50%;
    background: var(--white);
  }
  .brand-name {
    position: absolute;
    left: 804px;
    top: 72px;
    font-size: 38px;
    font-weight: 500;
    line-height: 36px;
    white-space: nowrap;
  }
  .brand-name span { display: block; }
</style>
</head>
<body>
  <section class="banner">
    <div class="banner-backdrop" role="img" aria-label="Blue backdrop with a faint world map, stock chart bars and grid lines"></div>
    <svg class="banner-wave" viewBox="0 0 1151 287" aria-hidden="true">
      <defs>
        <linearGradient id="waveFill" x1="0" y1="0" x2="1" y2="0">
          <stop offset="0" stop-color="#0d6fc6"/>
          <stop offset="0.48" stop-color="#80c6fb"/>
          <stop offset="0.6" stop-color="#7cc2f8"/>
          <stop offset="0.82" stop-color="#0a64bf"/>
          <stop offset="1" stop-color="#0565bd"/>
        </linearGradient>
      </defs>
      <path d="M0 219 C80 200 160 196 236 196 C380 196 460 215 560 235 C650 250 720 252 790 251 C950 250 1100 240 1151 208 L1151 287 L0 287 Z" fill="url(#waveFill)"/>
      <path d="M0 219 C80 200 160 196 236 196 C380 196 460 215 560 235 C650 250 720 252 790 251 C950 250 1100 240 1151 208" fill="none" stroke="#ffffff" stroke-width="2.5"/>
    </svg>
    <h1 class="headline">
      <span class="headline-strong">DATA-DRIVEN STOCK MARKET PORTFOLIO</span>
      <span class="headline-light">MANAGEMENT USING QUANTITATIVE ANALYSIS.</span>
    </h1>
    <div class="divider"></div>
    <div class="brand-dot"></div>
    <div class="brand-name">
      <span>QUANTLINE</span>
      <span>PORTFOLIO</span>
    </div>
  </section>
</body>
</html>
```